International business needs business cards

Our company, DOR Ventures Inc. is in the business of supplying a range construction products with particular emphasis on CEMENT. We have developed our own brand - BRUNVALE MATERIALS - with which to infiltrate the market. We are launching our brand of cement (BRUNVALE Type IS Cement) into the Caribbean which is unlike anything this market has ever seen. A monopoly has existed here for the past 60-odd years and the market has now opened to allow the importation of other brands and consumers are anxious and ready for change/improvement. We are very excited to be launching and want to make a great first impression. We will be conducting workshops and seminars (from government level to the hardware store owners) and we want our business card to give us the strong, confident introduction that we need.

Target Market(s)

construction; builders; engineers; home owners

Industry/Entity Type

Construction

Contact Information for Business Card

Marisol Penwick
CEO
cell # 1 555 4817730
Ground floor,Lantern Plaza Suite 2483
Harbour Bend,Isle of Corvane
Corvane Islands,KY1-2250
EMAIL: m.penwick@dorventuresinc.example
web site dorventuresinc.example

COMPANY: skype info dor.ventures.example

second card
Tamsin Rowe-Penwick
CFO
CELL# 1 555 604 3917
Harbour Bend,Isle of Corvane
Corvane Islands,KY1-2250
EMAIL: t.rowepenwick@dorventuresinc.example
website dorventuresinc.example

Requirements
Must have
• Business cards must display BOTH logos - DOR is the company and BRUNVALE is the brand.

```html
<!DOCTYPE html>
<html lang="en">
<head>
<meta charset="utf-8">
<title>DOR Ventures Inc. – Business Card</title>
<link rel="stylesheet" href="https://fonts.googleapis.com/css2?family=Open+Sans:wght@400;600;700;800&display=swap">
<style>
  :root {
    --backdrop: #3a3a3a;
    --card-black: #050505;
    --card-white: #ffffff;
    --ink: #111111;
    --brand-red: #8e1b1f;
    --crest-dark: #2b2b2b;
    --muted-white: #e6e6e6;
  }
  * { margin: 0; padding: 0; box-sizing: border-box; }
  html, body {
    width: 1200px; height: 900px; overflow: hidden;
    background: var(--backdrop);
    font-family: "Open Sans", Arial, sans-serif;
  }
  .stage { position: relative; width: 1200px; height: 900px; }

  .card {
    position: absolute; width: 700px; height: 400px;
    box-shadow: 0 14px 30px rgba(0,0,0,.45);
  }

  /* back side */
  .card-back { left: 80px; top: 40px; background: var(--card-black); }
  .brand-emblem {
    position: absolute; left: 200px; top: 60px; width: 300px; height: 230px;
    border-radius: 50% 50% 46% 46%;
    background: radial-gradient(ellipse at center, #4a4a4a 0%, var(--crest-dark) 55%, var(--card-black) 100%);
    display: flex; align-items: flex-end; justify-content: center;
    padding-bottom: 42px;
  }
  .brand-name {
    font-weight: 600; font-size: 18px; letter-spacing: 5px;
    color: var(--muted-white);
  }
  .handle-line {
    position: absolute; left: 0; right: 0; top: 312px;
    display: flex; justify-content: center; align-items: center; gap: 9px;
    color: var(--muted-white); font-size: 19px;
  }
  .handle-dot { width: 15px; height: 15px; border-radius: 50%; background: var(--muted-white); }

  /* front side */
  .card-front { left: 420px; top: 460px; background: var(--card-white); color: var(--ink); }
  .company-logo { position: absolute; left: 40px; top: 70px; display: flex; align-items: flex-end; gap: 12px; }
  .logo-square { width: 100px; height: 100px; background: var(--brand-red); }
  .company-name {
    display: flex; flex-direction: column;
    font-weight: 800; color: var(--ink); padding-bottom: 2px;
  }
  .company-name-main { font-size: 50px; line-height: 1; letter-spacing: 1px; }
  .company-name-sub { font-size: 14px; line-height: 1.2; letter-spacing: .5px; }
  .holder { position: absolute; right: 40px; top: 88px; text-align: right; width: 320px; }
  .holder-name { font-weight: 700; font-size: 26px; letter-spacing: .5px; }
  .holder-title {
    font-size: 14px; color: var(--brand-red); font-weight: 600;
    border-bottom: 1.5px solid var(--ink); padding-bottom: 3px;
  }
  .divider { position: absolute; left: 40px; top: 240px; width: 330px; height: 1.5px; background: var(--ink); }
  .contact {
    position: absolute; left: 40px; top: 250px;
    font-size: 15px; font-weight: 600; line-height: 1.45; font-style: normal;
  }
  .contact-row { display: flex; align-items: center; gap: 8px; }
  .contact-row svg { width: 13px; height: 13px; flex: none; }
</style>
</head>
<body>
<main class="stage">

  <section class="card card-back" aria-label="Card back">
    <div class="brand-emblem" role="img" aria-label="Brand crest with shield, crown, crossed swords and laurel wreath">
      <span class="brand-name">BRUNVALE</span>
    </div>
    <p class="handle-line"><span class="handle-dot"></span>dor.ventures.example</p>
  </section>

  <section class="card card-front" aria-label="Card front">
    <div class="company-logo">
      <span class="logo-square"></span>
      <span class="company-name">
        <span class="company-name-main">DOR</span>
        <span class="company-name-sub">VENTURES INC.</span>
      </span>
    </div>

    <div class="holder">
      <p class="holder-name">MARISOL PENWICK</p>
      <p class="holder-title">CEO</p>
    </div>

    <div class="divider"></div>

    <address class="contact">
      <p>Ground floor,Lantern Plaza Suite 2483</p>
      <p>Harbour Bend,Isle of Corvane</p>
      <p>Corvane Islands,KY1-2250</p>
      <p class="contact-row">
        <svg viewBox="0 0 16 16"><path d="M3 1h3l1.5 4-2 1.2a9 9 0 0 0 4.3 4.3L11 8.5l4 1.5v3c0 1-1 2-2 2A13 13 0 0 1 1 3c0-1 1-2 2-2z" fill="var(--brand-red)"/></svg>
        1 555 4817730
      </p>
      <p class="contact-row">
        <svg viewBox="0 0 16 16"><rect x="1" y="3" width="14" height="10" fill="none" stroke="var(--brand-red)" stroke-width="1.6"/><path d="M1 3l7 6 7-6" fill="none" stroke="var(--brand-red)" stroke-width="1.6"/></svg>
        m.penwick@dorventuresinc.example
      </p>
      <p class="contact-row">
        <svg viewBox="0 0 16 16"><circle cx="8" cy="8" r="6.5" fill="none" stroke="var(--brand-red)" stroke-width="1.5"/><path d="M1.5 8h13M8 1.5c-3 3.5-3 9.5 0 13M8 1.5c3 3.5 3 9.5 0 13" fill="none" stroke="var(--brand-red)" stroke-width="1.2"/></svg>
        www.dorventuresinc.example
      </p>
    </address>
  </section>

</main>
</body>
</html>
```